Indie film - female coming of age - Poster

poster for an indie film.
coming of age story about a young girl who is taken in by a wealthy 50 year old perennial bachelor who becomes her mentor.

The idea of the film is that you have to be lost to be found. There are two people who are lonely, and who save each other. One happens to be a high school girl, and the other is a fifty year old man. I guess I am looking for a sense of loneliness and longing. Two outsiders who find each other?

Target Market(s)

18-35

Industry/Entity Type

Film Production

Requirements
Must have
• we have included stills from the film for use as well as some designs from other film posters that we like for inspiration.
• An Quiet Harbor / Lantern Grove Production
• in Association with Velvet Orchard Pictures
• Tide Before Dawn
• Written & Directed by Claire-Louise Dorn
• Produced by Gregory Pambrick
• Executive Produced by Dennis Falcroft
Nice to have
• Actors names:
• Tessa Wrenby
• Corey Nash
• Taglines to try:
• Some relationships are hard to explain.
• Sometimes you have to be lost, in order to be found.

```html
<!DOCTYPE html>
<html lang="en">
<head>
<meta charset="utf-8">
<title>Tide Before Dawn — Poster</title>
<link rel="stylesheet" href="https://fonts.googleapis.com/css2?family=Raleway:wght@200;300&family=Oswald:wght@500;600&family=Roboto+Condensed:wght@400;700&display=swap">
<style>
  :root {
    --page: #eceae6;
    --frame-black: #0c0a10;
    --edge-cream: #efe3d2;
    --sky-top: #3e3260;
    --sky-mid: #7b6894;
    --haze-pale: #cdbfd4;
    --stage-dark: #241a2c;
    --stage-deep: #1c1530;
    --band: #1a1431;
    --title: #fbf8fb;
    --subtitle: #f6e7ea;
    --label: #e69a66;
    --name: #f1c27e;
    --fine: #8f84ab;
    --credit-top: #1f1a33;
  }
  * { margin: 0; padding: 0; box-sizing: border-box; }
  html, body {
    width: 1200px; height: 1148px; overflow: hidden;
    background: var(--page);
  }
  .poster {
    position: absolute; left: 200px; top: 24px;
    width: 800px; height: 1100px;
    background: var(--frame-black);
    padding: 10px;
  }
  .poster-sheet {
    position: relative; width: 100%; height: 100%;
    border: 6px solid var(--edge-cream);
    overflow: hidden;
    background: var(--sky-top);
  }
  .key-art {
    position: absolute; inset: 0;
    background:
      /* stage light from above */
      radial-gradient(ellipse 22% 18% at 58% 40%, rgba(214,200,222,0.75) 0%, rgba(214,200,222,0) 100%),
      /* pale highlight centre */
      radial-gradient(ellipse 16% 16% at 44% 44%, rgba(232,224,236,0.85) 0%, rgba(232,224,236,0) 100%),
      radial-gradient(ellipse 12% 14% at 52% 66%, rgba(196,186,206,0.75) 0%, rgba(196,186,206,0) 100%),
      /* dark lower masses */
      radial-gradient(ellipse 26% 30% at 30% 78%, rgba(36,26,44,0.95) 0%, rgba(36,26,44,0) 100%),
      radial-gradient(ellipse 28% 26% at 74% 68%, rgba(40,30,48,0.9) 0%, rgba(40,30,48,0) 100%),
      radial-gradient(ellipse 60% 22% at 50% 86%, rgba(30,22,42,0.85) 0%, rgba(30,22,42,0) 100%),
      /* clouds */
      radial-gradient(ellipse 40% 18% at 28% 18%, rgba(176,160,194,0.6) 0%, rgba(176,160,194,0) 100%),
      radial-gradient(ellipse 36% 16% at 74% 30%, rgba(186,170,200,0.55) 0%, rgba(186,170,200,0) 100%),
      radial-gradient(ellipse 30% 14% at 86% 8%, rgba(40,32,66,0.8) 0%, rgba(40,32,66,0) 100%),
      /* corner vignette */
      radial-gradient(ellipse 90% 80% at 50% 45%, rgba(0,0,0,0) 55%, rgba(22,16,38,0.55) 100%),
      linear-gradient(180deg, #4a3d6c 0%, var(--sky-mid) 30%, #6c5b8a 52%, #4d3f68 74%, var(--stage-deep) 100%);
  }
  .production-line {
    position: absolute; top: 34px; left: 0; right: 0;
    text-align: center; color: var(--credit-top);
    font-family: "Roboto Condensed", sans-serif; font-weight: 700;
    text-transform: uppercase; line-height: 1.45;
  }
  .production-line .main { font-size: 17px; letter-spacing: 0.3px; }
  .production-line .assoc { font-size: 15px; }
  .production-line small { font-size: 11px; font-weight: 700; }
  .title-main {
    position: absolute; top: 122px; left: 0; right: 0;
    text-align: center; color: var(--title);
    font-family: "Raleway", sans-serif; font-weight: 200;
    font-size: 132px; letter-spacing: 8px; line-height: 1;
  }
  .title-sub {
    position: absolute; top: 262px; left: 0; right: 0;
    display: flex; justify-content: center; align-items: center; gap: 16px;
    color: var(--subtitle);
    font-family: "Oswald", sans-serif; font-weight: 600;
    font-size: 48px; letter-spacing: 1px; line-height: 1;
  }
  .title-rule { width: 110px; height: 14px; }
  .credit-band {
    position: absolute; left: 0; right: 0; bottom: 0; height: 200px;
    background: linear-gradient(180deg, rgba(26,20,49,0.78) 0%, rgba(26,20,49,0.95) 30%, var(--band) 60%);
    padding: 26px 30px 0;
  }
  .credit-columns {
    display: flex; justify-content: space-between;
    font-family: "Roboto Condensed", sans-serif; text-transform: uppercase;
    text-align: center;
  }
  .credit { width: 33%; }
  .credit-label { color: var(--label); font-size: 15px; letter-spacing: 0.3px; }
  .credit-name { color: var(--name); font-size: 17px; font-weight: 700; margin-top: 2px; }
  .credit-fine {
    margin-top: 18px; text-align: center; color: var(--fine);
    font-family: "Roboto Condensed", sans-serif; text-transform: uppercase;
    font-size: 12px; line-height: 1.55; letter-spacing: 0.2px;
  }
</style>
</head>
<body>
  <main class="poster">
    <div class="poster-sheet">
      <div class="key-art" role="img" aria-label="Film still: a young blonde singer in a dark fringed jacket holding a microphone, head tilted back and arm outstretched, against a hazy violet sky of clouds and stage light"></div>

      <header class="production-line">
        <p class="main"><small>An</small> Quiet Harbor / Lantern Grove Production</p>
        <p class="assoc"><small>in association with</small> Velvet Orchard Pictures</p>
      </header>

      <h1 class="title-main">TIDE</h1>
      <div class="title-sub">
        <svg class="title-rule" viewBox="0 0 110 14" aria-hidden="true">
          <g stroke="#e9dbe4" stroke-width="1"><line x1="0" y1="2" x2="110" y2="2"/><line x1="0" y1="7" x2="110" y2="7"/><line x1="0" y1="12" x2="110" y2="12"/></g>
        </svg>
        <span>BEFORE DAWN</span>
        <svg class="title-rule" viewBox="0 0 110 14" aria-hidden="true">
          <g stroke="#e9dbe4" stroke-width="1"><line x1="0" y1="2" x2="110" y2="2"/><line x1="0" y1="7" x2="110" y2="7"/><line x1="0" y1="12" x2="110" y2="12"/></g>
        </svg>
      </div>

      <footer class="credit-band">
        <div class="credit-columns">
          <div class="credit">
            <p class="credit-label">Written &amp; Directed by</p>
            <p class="credit-name">Claire-Louise Dorn</p>
          </div>
          <div class="credit">
            <p class="credit-label">Produced by</p>
            <p class="credit-name">Gregory Pambrick</p>
          </div>
          <div class="credit">
            <p class="credit-label">Executive Produced by</p>
            <p class="credit-name">Dennis Falcroft</p>
          </div>
        </div>
        <p class="credit-fine">Starring Tessa Wrenby and Corey Nash. Some relationships are hard to explain. Sometimes you have to be lost in order to be found. Music by Hollis Vantree. Edited by Marta Quillon. Director of photography Sven Adderly. Production design by Ines Carrow. Casting by Ruth Ellamy. Costume design by Nadia Frell. Co-produced by Owen Brask and Lila Fenwick.</p>
      </footer>
    </div>
  </main>
</body>
</html>
```